Musical Instrument Store Needs Band Instrument Postcard to Upgrade Current Customers

We need a new postcard design to mail to our current instrument rental customers. People start out renting a student line/beginner instrument and we want to emphasize our upgrade program that allows them to apply the equity from their beginner instrument to an intermediate or professional instrument. I have attached an image of the front (Velmora Postcard Front) and back (Velmora Postcard Back) of what we have used in the past. The back still needs to have all the information currently on it. The front can be whatever you come up with (I don't necessarily care for our current design), but should include the tagline "Reach Your Full Potential". Also, if there is more room on the front or back, it would be nice to have a brief mention of our lesson studio (I have also included our lesson studio postcard for ideas).

There are also pictures of each instrument attached. There are a few for the trumpet so you can decide which one would work best.

Target Market(s)

Current instrument rental customers

Industry/Entity Type

Store

Requirements
Must have
• The back of postcard must have all the information from the file "Velmora Postcard Back". The front should have the tagline "Reach Your Full Potential". Pictures of the instruments should be on the front as well.
Nice to have
• A brief mention or reminder that we have a large lesson studio with highly qualified instructors.

```html
<!DOCTYPE html>
<html lang="en">
<head>
<meta charset="utf-8">
<title>Velmora Music Center – Step-Up Postcard</title>
<link rel="stylesheet" href="https://fonts.googleapis.com/css2?family=Barlow:wght@500;700&family=Barlow+Condensed:wght@500&display=swap">
<style>
  :root {
    --backdrop: #c4c4c4;
    --card-white: #ffffff;
    --photo-base: #8a888b;
    --brass: #a89a6e;
    --silver: #b3b1b4;
    --ebony: #4a4552;
    --rule-white: #f4f4f4;
    --headline-white: rgba(255, 255, 255, 0.94);
    --ink: #111111;
    --faint-photo: #e8e8e8;
  }
  * { margin: 0; padding: 0; box-sizing: border-box; }
  html, body {
    width: 920px;
    height: 1200px;
    overflow: hidden;
    background: var(--backdrop);
  }
  .canvas { position: relative; width: 920px; height: 1200px; }
  .postcard {
    position: absolute;
    left: 18px;
    width: 900px;
    overflow: hidden;
    box-shadow: 3px 4px 8px rgba(0, 0, 0, 0.35);
  }
  /* Front */
  .postcard-front { top: 24px; height: 582px; background: var(--photo-base); }
  .instrument-photos { position: absolute; inset: 0; display: block; }
  .front-rule {
    position: absolute;
    left: 87px;
    width: 700px;
    height: 6px;
    background: var(--rule-white);
  }
  .front-rule.top { top: 74px; }
  .front-rule.bottom { top: 508px; }
  .tagline {
    position: absolute;
    left: 0;
    right: 0;
    top: 128px;
    text-align: center;
    font-family: "Barlow Condensed", sans-serif;
    font-weight: 500;
    font-size: 140px;
    line-height: 145px;
    letter-spacing: -4px;
    color: var(--headline-white);
    text-transform: uppercase;
  }
  /* Back */
  .postcard-back { top: 620px; height: 580px; background: var(--card-white); }
  .faded-photo {
    position: absolute;
    left: 0;
    top: 0;
    width: 500px;
    height: 100%;
    background: linear-gradient(90deg, var(--faint-photo) 0%, #f0f0f0 65%, var(--card-white) 100%);
  }
  .back-content {
    position: absolute;
    left: 50px;
    top: 0;
    width: 330px;
    height: 100%;
    color: var(--ink);
    font-family: "Barlow", sans-serif;
    font-weight: 500;
  }
  .store-name {
    position: absolute;
    top: 56px;
    font-weight: 700;
    font-size: 26px;
    line-height: 30px;
    white-space: nowrap;
  }
  .contact {
    position: absolute;
    top: 109px;
    font-size: 15.5px;
    line-height: 19px;
    font-style: normal;
  }
  .offer {
    position: absolute;
    top: 228px;
    width: 318px;
    font-size: 16.5px;
    line-height: 23px;
  }
  .offer p + p { margin-top: 14px; }
  .highlights {
    position: absolute;
    top: 473px;
    list-style: none;
    font-size: 20px;
    line-height: 24px;
    text-transform: uppercase;
    white-space: nowrap;
  }
  .highlights li + li { margin-top: 12px; }
</style>
</head>
<body>
<main class="canvas">
  <section class="postcard postcard-front">
    <svg class="instrument-photos" width="900" height="582" viewBox="0 0 900 582" role="img" aria-label="Photographs of band instruments laid diagonally: clarinets, flutes, a saxophone, trumpets and trombones">
      <defs>
        <linearGradient id="brass-tone" x1="0" y1="0" x2="1" y2="0">
          <stop offset="0" stop-color="#8f8466"/><stop offset="0.5" stop-color="var(--brass)"/><stop offset="1" stop-color="#8f8466"/>
        </linearGradient>
        <linearGradient id="silver-tone" x1="0" y1="0" x2="1" y2="0">
          <stop offset="0" stop-color="#9c9a9d"/><stop offset="0.5" stop-color="var(--silver)"/><stop offset="1" stop-color="#9c9a9d"/>
        </linearGradient>
      </defs>
      <g transform="rotate(-35 450 291)" opacity="0.75">
        <rect x="-300" y="-40" width="1500" height="26" fill="url(#silver-tone)"/>
        <rect x="-300" y="40" width="1500" height="30" fill="var(--ebony)"/>
        <rect x="-300" y="120" width="1500" height="22" fill="url(#silver-tone)"/>
        <rect x="-300" y="190" width="1500" height="46" fill="url(#silver-tone)"/>
        <rect x="-300" y="280" width="1500" height="34" fill="url(#brass-tone)"/>
        <rect x="-300" y="360" width="1500" height="40" fill="url(#silver-tone)"/>
        <rect x="-300" y="440" width="1500" height="30" fill="var(--ebony)"/>
        <rect x="-300" y="520" width="1500" height="36" fill="url(#brass-tone)"/>
        <rect x="-300" y="600" width="1500" height="22" fill="url(#silver-tone)"/>
      </g>
      <rect width="900" height="582" fill="#6e6c70" opacity="0.35"/>
    </svg>
    <div class="front-rule top"></div>
    <h1 class="tagline">Reach Your<br>Full Potential</h1>
    <div class="front-rule bottom"></div>
  </section>

  <section class="postcard postcard-back">
    <div class="faded-photo" role="img" aria-label="Faded pale photograph of band instruments behind the text"></div>
    <div class="back-content">
      <div class="store-name">Velmora Music Center</div>
      <address class="contact">
        2718 Larkspur Ave. NW<br>
        Brookfield, OH 44900<br>
        330-555-0142<br>
        877-555-0142 (toll free)
      </address>
      <div class="offer">
        <p>Your student is ready to Step-Up to a Soloist Performance Instrument. To make it easier, you may apply equity from the instrument you are currently renting towards the upgraded Soloist Performance or Artist Series Instrument.</p>
        <p>Please call to set up your private appointment.</p>
      </div>
      <ul class="highlights">
        <li>Large Lesson Studio!</li>
        <li>Highly Qualified Instructors!</li>
      </ul>
    </div>
  </section>
</main>
</body>
</html>
```